Stationery Design Project

Please create a custom Stationery Design for Brookfern Homes. The logo is attached to this brief.

Please Include:
- Letterhead
- With Compliments slip
- Envelope

Please also see open Business Card project: http://tasks.pixelbazaar-example.com/task.aspx?id=517290

Industry/Entity Type

Business

```html
<!DOCTYPE html>
<html lang="en">
<head>
<meta charset="utf-8">
<title>Brookfern Homes Stationery</title>
<link rel="stylesheet" href="https://fonts.googleapis.com/css2?family=Open+Sans:wght@400;600&family=Tinos&family=Great+Vibes&display=swap">
<style>
  :root {
    --board: #0b0b0c;
    --paper: #f7f7f7;
    --paper-edge: #d8d8d8;
    --brand-blue: #0a6ab5;
    --brand-yellow: #f7c700;
    --ghost: #ececec;
    --ink: #333333;
  }
  * { margin: 0; padding: 0; box-sizing: border-box; }
  html, body { width: 1200px; height: 900px; overflow: hidden; background: var(--board); }
  .board { position: relative; width: 1200px; height: 900px; background: var(--board); }

  .sheet { position: absolute; background: var(--paper); border: 1px solid var(--paper-edge); overflow: hidden; }
  .card { border-radius: 10px; }

  .envelope { left: 79px; top: 130px; width: 517px; height: 249px; }
  .card-front { left: 79px; top: 399px; width: 248px; height: 139px; }
  .card-back { left: 348px; top: 399px; width: 248px; height: 139px; }
  .comp-slip { left: 79px; top: 564px; width: 517px; height: 207px; }
  .letterhead { left: 671px; top: 130px; width: 453px; height: 641px; }

  .ghost-mark { position: absolute; border-radius: 50%; background: var(--ghost); }

  .brand { position: absolute; display: flex; flex-direction: column; align-items: center; }
  .brand-dot { border-radius: 50%; background: var(--brand-yellow); }
  .brand-name {
    font-family: "Open Sans", Arial, sans-serif; font-weight: 600; color: var(--brand-blue);
    text-transform: uppercase; text-align: center; line-height: 1.15;
  }

  .contact-line {
    position: absolute; font-family: "Tinos", "Times New Roman", serif;
    font-size: 9.5px; color: var(--ink); white-space: nowrap;
  }

  .card-details {
    position: absolute; font-family: "Open Sans", Arial, sans-serif; font-size: 6.5px;
    color: var(--ink); line-height: 1.4;
  }
  .card-details .person { font-size: 7px; margin-bottom: 2px; }

  .comp-title {
    position: absolute; left: 22px; top: 26px; font-family: "Great Vibes", cursive;
    font-size: 26px; color: #222;
  }
</style>
</head>
<body>
<main class="board">

  <section class="sheet envelope" aria-label="Envelope">
    <div class="ghost-mark" style="left:290px; top:10px; width:210px; height:210px;"></div>
    <div class="brand" style="left:18px; top:120px; width:70px;">
      <div class="brand-dot" style="width:32px; height:32px; margin-bottom:8px;"></div>
      <div class="brand-name" style="font-size:10px;">Brookfern<br>Homes</div>
    </div>
    <p class="contact-line" style="left:21px; top:214px;">PO Box 482113, Riverton, NZ.&nbsp;&nbsp;&nbsp;T : + 22 174 5560&nbsp;&nbsp;&nbsp;F : + 22 174 5563&nbsp;&nbsp;&nbsp;E : mara@brookfernhomes.nz</p>
  </section>

  <section class="sheet card card-front" aria-label="Business card front">
    <div class="brand" style="left:18px; top:36px; width:66px;">
      <div class="brand-dot" style="width:26px; height:26px; margin-bottom:7px;"></div>
      <div class="brand-name" style="font-size:8.5px;">Brookfern<br>Homes</div>
    </div>
    <div class="card-details" style="left:106px; top:21px;">
      <p class="person">MARA TELLER</p>
      <p>DIRECTOR</p>
      <p>C. : +22 9473015286</p>
    </div>
    <div class="card-details" style="left:106px; top:85px;">
      <p>PO Box 482113, Riverton, NZ.</p>
      <p>T : + 22 174-5581</p>
      <p>F : + 22 174-5584</p>
      <p>E : mara@brookfernhomes.nz</p>
    </div>
  </section>

  <section class="sheet card card-back" aria-label="Business card back">
    <div class="ghost-mark" style="left:40px; top:5px; width:130px; height:130px;"></div>
    <div class="brand" style="left:74px; top:28px; width:100px;">
      <div class="brand-dot" style="width:36px; height:36px; margin-bottom:8px;"></div>
      <div class="brand-name" style="font-size:11px;">Brookfern<br>Homes</div>
    </div>
  </section>

  <section class="sheet comp-slip" aria-label="With compliments slip">
    <div class="ghost-mark" style="left:290px; top:30px; width:170px; height:170px;"></div>
    <h2 class="comp-title">With Compliments</h2>
    <div class="brand" style="left:18px; top:78px; width:70px;">
      <div class="brand-dot" style="width:32px; height:32px; margin-bottom:8px;"></div>
      <div class="brand-name" style="font-size:10px;">Brookfern<br>Homes</div>
    </div>
    <p class="contact-line" style="left:21px; top:171px;">PO Box 482113, Riverton, NZ.&nbsp;&nbsp;&nbsp;T : + 22 174 5560&nbsp;&nbsp;&nbsp;F : + 22 174 5563&nbsp;&nbsp;&nbsp;E : mara@brookfernhomes.nz</p>
  </section>

  <section class="sheet letterhead" aria-label="Letterhead">
    <div class="brand" style="left:136px; top:18px; width:180px;">
      <div class="brand-dot" style="width:70px; height:70px; margin-bottom:14px;"></div>
      <div class="brand-name" style="font-size:18px;">Brookfern<br>Homes</div>
    </div>
    <div class="ghost-mark" style="left:118px; top:245px; width:220px; height:220px;"></div>
    <p class="contact-line" style="left:12px; top:601px;">PO Box 482113, Riverton, NZ.&nbsp;&nbsp;&nbsp;T : + 22 174 5560&nbsp;&nbsp;&nbsp;F : + 22 174 5563&nbsp;&nbsp;&nbsp;E : mara@brookfernhomes.nz</p>
  </section>

</main>
</body>
</html>
```